Business Card Design for Small Electrical Contractor

I need to update my business card into something a little more modern. We are a small electrical contracting company. We service domestic and commercial places around Sydney. We have 2 logo designs at the moment. I have uploaded both and 2 different sizes to work with.

Industry/Entity Type

Business

Contact Information for Business Card

Ted Corbin
8/21-23 Holt St, Fernhaven 2087
t - (02) 9471 3820
m - 0427 915 304
E - info@corbinelec.example.au
W - corbinelec.example.au
ABN: 42 907 518 263

Font styles to use
Sans Serif

Requirements
Must have
• I would also like to see the below fit on somewhere aswell
• - Licensed Electrician
• - Level 2 (Cat 1 & 4)
• - Domestic
• - Commercial
• - Repairs and Installations
• - Data
Nice to have
• Try and keep similar colours as logo
Should not have
• No lightning bolts or light globes. Smart and professional please.

```html
<!DOCTYPE html>
<html lang="en">
<head>
<meta charset="utf-8">
<title>Corbin Electrical – Business Card</title>
<link rel="stylesheet" href="https://fonts.googleapis.com/css2?family=Open+Sans:ital,wght@0,400;0,600;0,700;1,400&display=swap">
<style>
  :root {
    --navy: #111a38;
    --orange: #dc8219;
    --paper: #e9e9ea;
    --ink: #2d3136;
    --ink-dark: #1d2a33;
    --backdrop: #9c9c9c;
    --line: #dc8219;
  }
  html, body {
    margin: 0;
    padding: 0;
    width: 1105px;
    height: 1200px;
    overflow: hidden;
    background: var(--backdrop);
    font-family: "Open Sans", Arial, sans-serif;
  }
  .canvas {
    position: relative;
    width: 1105px;
    height: 1200px;
  }
  .card {
    position: absolute;
    left: 182px;
    width: 747px;
    height: 425px;
    background: var(--paper);
    overflow: hidden;
  }
  .card--front { top: 119px; }
  .card--back { top: 637px; }

  /* Front */
  .brand-panel {
    position: absolute;
    left: 0; top: 0;
    width: 374px; height: 100%;
    background: var(--navy);
    display: flex;
    align-items: center;
    justify-content: center;
  }
  .brand-name {
    font-weight: 600;
    font-size: 34px;
    letter-spacing: 0.5px;
    line-height: 1;
    white-space: nowrap;
  }
  .brand-panel .brand-name { color: #ffffff; }
  .accent-strip {
    position: absolute;
    right: 0; top: 0;
    width: 25px; height: 100%;
    background: var(--orange);
  }
  .contact-panel {
    position: absolute;
    left: 374px; top: 0;
    width: 348px; height: 100%;
    text-align: center;
    color: var(--ink);
  }
  .person-name {
    margin: 48px 0 0;
    font-weight: 700;
    font-size: 24px;
    letter-spacing: 0.6px;
    color: var(--ink-dark);
    line-height: 1.2;
  }
  .person-role {
    margin: 2px 0 0;
    font-size: 19px;
    line-height: 1.45;
    color: var(--orange);
  }
  .address {
    margin: 28px 0 0;
    font-size: 19px;
    line-height: 1.5;
  }
  .contact-list {
    list-style: none;
    margin: 22px 0 0;
    padding: 0;
    font-size: 19px;
    line-height: 1.5;
  }
  .contact-list li {
    display: flex;
    align-items: center;
    justify-content: center;
    gap: 8px;
  }
  .contact-list svg {
    width: 17px;
    height: 17px;
    fill: var(--ink-dark);
    flex: none;
  }

  /* Back */
  .back-brand {
    position: absolute;
    left: 0; right: 0;
    top: 170px;
    text-align: center;
  }
  .back-brand .brand-name {
    color: var(--ink-dark);
    font-size: 44px;
  }
  .back-brand .rule {
    width: 360px;
    height: 2px;
    margin: 18px auto 0;
    background: var(--line);
  }
  .services {
    position: absolute;
    left: 0; right: 0;
    top: 330px;
    margin: 0;
    text-align: center;
    font-style: italic;
    font-size: 19px;
    line-height: 1.45;
    color: var(--ink);
  }
  .services .dot {
    display: inline-block;
    width: 8px; height: 8px;
    border-radius: 50%;
    background: var(--ink-dark);
    vertical-align: middle;
    margin: 0 4px;
  }
</style>
</head>
<body>
<main class="canvas">

  <section class="card card--front" aria-label="Business card front">
    <div class="brand-panel">
      <span class="brand-name">Corbin Electrical</span>
    </div>

    <div class="contact-panel">
      <h1 class="person-name">TED CORBIN</h1>
      <p class="person-role">Director<br>Licensed Electrician</p>
      <p class="address">8/21-23 Holt St<br>Fernhaven 2087<br>ABN: 42 907 518 263</p>
      <ul class="contact-list">
        <li>
          <svg viewBox="0 0 24 24" aria-hidden="true"><path d="M6.6 10.8a15.2 15.2 0 0 0 6.6 6.6l2.2-2.2a1 1 0 0 1 1-.25 11.4 11.4 0 0 0 3.6.57 1 1 0 0 1 1 1V20a1 1 0 0 1-1 1A17 17 0 0 1 3 4a1 1 0 0 1 1-1h3.5a1 1 0 0 1 1 1c0 1.25.2 2.45.57 3.57a1 1 0 0 1-.25 1z"/></svg>
          (02) 9471 3820
        </li>
        <li>
          <svg viewBox="0 0 24 24" aria-hidden="true"><path d="M7 1h10a2 2 0 0 1 2 2v18a2 2 0 0 1-2 2H7a2 2 0 0 1-2-2V3a2 2 0 0 1 2-2zm0 3v14h10V4zm5 15.2a1.2 1.2 0 1 0 0 2.4 1.2 1.2 0 0 0 0-2.4z"/></svg>
          0427 915 304
        </li>
        <li>
          <svg viewBox="0 0 24 24" aria-hidden="true"><path d="M2 5h20v14H2zm2 2v.5l8 5 8-5V7zm0 2.8V17h16V9.8l-8 5z"/></svg>
          info@corbinelec.example.au
        </li>
        <li>
          <svg viewBox="0 0 24 24" aria-hidden="true"><path d="M12 2a10 10 0 1 0 0 20 10 10 0 0 0 0-20zm-1 17.9A8 8 0 0 1 4.1 11H7v2l4 4zm6.9-2.5A2 2 0 0 0 16 16h-1v-3a1 1 0 0 0-1-1H8v-2h2a1 1 0 0 0 1-1V7h2a2 2 0 0 0 2-2v-.4a8 8 0 0 1 2.9 12.8z"/></svg>
          www.corbinelec.example.au
        </li>
      </ul>
    </div>

    <div class="accent-strip"></div>
  </section>

  <section class="card card--back" aria-label="Business card back">
    <div class="back-brand">
      <span class="brand-name">Corbin Electrical</span>
      <div class="rule"></div>
    </div>
    <p class="services">
      Domestic<span class="dot"></span>Commercial<span class="dot"></span>Repairs &amp; Installations.<br>
      Data<span class="dot"></span>Level 2 (Cat 1 &amp; 4)
    </p>
  </section>

</main>
</body>
</html>
```